Riverbend Trusted Home Care-Flyer for Patients

Our Home Health Care Agency, Riverbend Trusted Home Care, is seeking a flyer to advertise our services. We would like our flyer to convey professionalism, classiness and sophistication. We want our agency to come across as one that is well-established and recognized as being first-rate within the field.

We also want to appear original; we want to stand out.

Our theme colors, blue and green, from our logo should be incorporated into the flyer's design (refer below).

The top of the page should say (in a clear, bold font)-Seeking Care for your Loved One?

Our Logo, followed by our slogan, "Lean On Those Nearby", should be in the center. (This should make it appear as if our agency is the obvious solution to the consumer's quest in finding suitable care for their family member). This should be in a big font.
Below that, our agency's services should be listed in a very noticeable font...yet smaller than what's written above that.
The text should read:
Our Services Include:
*Experienced Certified Home Health Aides/ Live In Home Health Aides/Companions
*Nursing Services
*Alzheimer’s and Dementia Care
*Respite Care
*Postoperative Care
*Post Rehabilitation Care
*Running Errands
*Light Housekeeping
*Assistance with Bathing, Feeding and Grooming
*Meal Preparation
*Laundry and Linen Washing
*Mail and Bill Organization
*Medication Management
*Accompanying to Doctor’s Appointments
*And much more!
Below that, in a smaller, yet noticeable font:
As seasoned professionals, we know how to help our clients navigate and fulfill their various health care needs. Those nearby are here to help you get the attention that you merit.
Call Riverbend Trusted Home Care today to learn more about our first-rate services!
Below that, in a larger font, our phone number, website, our e-mail address.
*Out contact information will be provided to the project’s winner*.

*Pictures of Caregivers helping elderly patient should be included in the advertisement as well. *

We provided advertisements of other Home Health Care Agencies attached below to use as a reference. Once again, while we are aiming for a similar idea; however, our goal is to stand out as the community's premiere home health care agency, the one that they want to choose. We want to be original as well!

Size: Standard Computer Paper Size. 8.5” x 11”.

Feel free to utilize your creative, designer flair!
We look forward to seeing the results!
Good luck!

Industry/Entity Type

Home Health Care

Font styles to use
Sans Serif

Requirements
Must have
• Refer above.
Nice to have
• Refer to attachment below to see how other home health care agencies advertise. While we are aiming for a similar idea, we would like to incorporate our logo, slogan and colors to make this flyer more unique and stand out. We would like to appear original.

```html
<!DOCTYPE html>
<html lang="en">
<head>
<meta charset="utf-8">
<title>Riverbend Trusted Home Care – Patient Flyer</title>
<link rel="stylesheet" href="https://fonts.googleapis.com/css2?family=Oswald:wght@600;700&family=Roboto:wght@400;500;700&family=Montserrat:wght@400;500;700&display=swap">
<style>
  :root{
    --blue:#0d4f96;
    --blue-deep:#0a4384;
    --green:#8cc63f;
    --paper:#ffffff;
    --stage:#eeeeee;
    --ink:#1b1b1b;
  }
  *{margin:0;padding:0;box-sizing:border-box}
  html,body{width:701px;height:1200px;overflow:hidden;background:var(--stage)}
  .flyer{position:absolute;left:0;top:146px;width:701px;height:907px;background:var(--paper);overflow:hidden;box-shadow:0 2px 10px rgba(0,0,0,.15)}
  .abs{position:absolute}
  .headline{font-family:'Oswald',sans-serif;font-weight:700;line-height:1;letter-spacing:.2px}
  .question{left:28px;top:24px;font-size:45px;color:var(--blue)}
  .question .line2{display:block;color:var(--green);margin-top:4px}
  .rule{left:28px;top:137px;width:180px;height:3px;background:var(--green)}
  .slogan{left:30px;top:146px}
  .slogan .small{display:block;font-size:42px;color:var(--blue)}
  .slogan .big{display:block;font-size:64px;color:var(--blue);margin-top:2px}
  .slogan .big.green{color:var(--green);margin-top:2px}
  .brand{left:470px;top:24px;width:162px;text-align:center}
  .brand .dot{width:54px;height:54px;border-radius:50%;background:var(--blue);margin:0 auto 8px}
  .brand .name{font-family:'Roboto',sans-serif;font-weight:700;font-size:12px;line-height:1.2;color:var(--blue);letter-spacing:.3px}
  .portrait{left:425px;top:106px}
  .band{left:0;top:358px;width:701px;height:103px;background:var(--blue)}
  .band-photo{left:0;top:330px;width:204px;height:131px;border-radius:60px 60px 0 0}
  .band-text{left:221px;top:372px;width:470px;font-family:'Montserrat',sans-serif;font-weight:500;font-size:11.6px;line-height:15.2px;color:#fff}
  .services-title{left:30px;top:471px;font-family:'Roboto',sans-serif;font-weight:500;font-size:28px;color:var(--blue)}
  .services-rule{left:30px;top:509px;width:172px;height:1.5px;background:var(--green)}
  .services-rule-accent{left:57px;top:507px;width:43px;height:4px;background:var(--blue)}
  .service{display:flex;align-items:center;gap:8px;font-family:'Roboto',sans-serif;font-size:11.4px;line-height:13.5px;color:var(--ink)}
  .service svg{flex:none}
  .cta{left:20px;top:770px;width:663px;height:42px;border-radius:21px;background:var(--blue);color:#fff;font-family:'Montserrat',sans-serif;font-weight:500;font-size:21.5px;letter-spacing:.4px;display:flex;align-items:center;justify-content:center}
  .swoosh{left:0;top:0}
  .phone{left:33px;top:850px;font-family:'Montserrat',sans-serif;font-weight:700;font-size:28px;color:#fff;display:flex;align-items:center;gap:5px}
  .email{right:34px;top:823px;font-family:'Montserrat',sans-serif;font-weight:400;font-size:23px;color:var(--blue);display:flex;align-items:center;gap:10px}
  .web{right:34px;top:856px;font-family:'Montserrat',sans-serif;font-weight:700;font-size:24px;color:var(--blue-deep)}
  .base-line{left:0;top:903px;width:701px;height:4px;background:var(--green)}
</style>
</head>
<body>
<main class="flyer">

  <svg class="abs swoosh" width="701" height="907" viewBox="0 0 701 907" aria-hidden="true">
    <path d="M0 850 C60 818 180 812 250 850 C290 872 320 892 340 907 L0 907 Z" fill="var(--green)"/>
  </svg>

  <h1 class="abs headline question">Seeking Care for<span class="line2">Your Loved One?</span></h1>
  <div class="abs rule"></div>
  <h2 class="abs headline slogan"><span class="small">Lean On</span><span class="big">Those</span><span class="big green">Nearby</span></h2>

  <div class="abs brand">
    <div class="dot"></div>
    <div class="name">RIVERBEND TRUSTED<br>HOME CARE</div>
  </div>

  <svg class="abs portrait" width="260" height="260" viewBox="0 0 260 260">
    <defs>
      <radialGradient id="seniorsTone" cx="50%" cy="45%" r="60%">
        <stop offset="0" stop-color="#e9d7bf"/>
        <stop offset=".6" stop-color="#c9b79e"/>
        <stop offset="1" stop-color="#9a9a8e"/>
      </radialGradient>
    </defs>
    <path d="M200 38 A118 118 0 1 0 195 225" fill="none" stroke="var(--green)" stroke-width="8" stroke-linecap="round"/>
    <path d="M60 230 Q130 262 205 222" fill="none" stroke="var(--blue)" stroke-width="6" stroke-linecap="round"/>
    <circle cx="136" cy="128" r="106" fill="url(#seniorsTone)" role="img" aria-label="Photo of a smiling senior couple, a man with a cane and a woman in a yellow cardigan"/>
  </svg>

  <div class="abs band"></div>
  <div class="abs band-photo" role="img" aria-label="Photo of a caregiver holding the hands of an elderly patient in bed" style="background:linear-gradient(135deg,#d9cfc6 0%,#a9bcd6 45%,#e6e9ef 100%)"></div>
  <p class="abs band-text">As seasoned professionals, we know how to help our clients navigate and fulfill their various health care needs. Those nearby are here to help you get the attention that you merit.<br>Call Riverbend Trusted Home Care today to learn more about our first-rate services!</p>

  <h3 class="abs services-title">Our Services Include</h3>
  <div class="abs services-rule"></div>
  <div class="abs services-rule-accent"></div>

  <!-- service icon ring reused -->
  <svg width="0" height="0" style="position:absolute" aria-hidden="true">
    <defs>
      <g id="ring">
        <circle cx="20" cy="20" r="16" fill="#fff" stroke="var(--blue)" stroke-width="3"/>
        <path d="M10 36 A18.5 18.5 0 0 1 10 4" fill="none" stroke="var(--green)" stroke-width="2"/>
        <path d="M16 20h8M20 16v8" stroke="var(--blue)" stroke-width="2.2" stroke-linecap="round"/>
      </g>
    </defs>
  </svg>

  <div class="abs service" style="left:31px;top:523px"><svg width="40" height="40"><use href="#ring"/></svg><span>Experienced Certified Home Health Aides/<br>Live In Home Health Aides/Companions</span></div>
  <div class="abs service" style="left:31px;top:573px"><svg width="40" height="40"><use href="#ring"/></svg><span>Nursing Services</span></div>
  <div class="abs service" style="left:31px;top:620px"><svg width="40" height="40"><use href="#ring"/></svg><span>Alzheimer’s and Dementia Care</span></div>
  <div class="abs service" style="left:31px;top:670px"><svg width="40" height="40"><use href="#ring"/></svg><span>Respite Care</span></div>
  <div class="abs service" style="left:31px;top:719px"><svg width="40" height="40"><use href="#ring"/></svg><span>Medication Management</span></div>

  <div class="abs service" style="left:309px;top:523px"><svg width="40" height="40"><use href="#ring"/></svg><span>Postoperative Care</span></div>
  <div class="abs service" style="left:309px;top:573px"><svg width="40" height="40"><use href="#ring"/></svg><span>Post Rehabilitation Care</span></div>
  <div class="abs service" style="left:309px;top:620px"><svg width="40" height="40"><use href="#ring"/></svg><span>Running Errands</span></div>
  <div class="abs service" style="left:309px;top:670px"><svg width="40" height="40"><use href="#ring"/></svg><span>Light Housekeeping</span></div>
  <div class="abs service" style="left:309px;top:719px"><svg width="40" height="40"><use href="#ring"/></svg><span>Accompanying to Doctor’s Appointments</span></div>

  <div class="abs service" style="left:482px;top:523px"><svg width="40" height="40"><use href="#ring"/></svg><span>Assistance with Bathing,<br>Feeding and Grooming</span></div>
  <div class="abs service" style="left:482px;top:573px"><svg width="40" height="40"><use href="#ring"/></svg><span>Meal Preparation</span></div>
  <div class="abs service" style="left:482px;top:620px"><svg width="40" height="40"><use href="#ring"/></svg><span>Laundry and Linen<br>Washing</span></div>
  <div class="abs service" style="left:482px;top:670px"><svg width="40" height="40"><use href="#ring"/></svg><span>Mail and Bill Organization</span></div>

  <div class="abs cta">Call Today to Hear About Our First-rate Services</div>

  <div class="abs phone">
    <svg width="22" height="22" viewBox="0 0 24 24" aria-hidden="true"><path fill="#fff" d="M6.6 10.8a15.1 15.1 0 0 0 6.6 6.6l2.2-2.2a1 1 0 0 1 1-.25c1.1.37 2.3.57 3.6.57a1 1 0 0 1 1 1V20a1 1 0 0 1-1 1A17 17 0 0 1 3 4a1 1 0 0 1 1-1h3.5a1 1 0 0 1 1 1c0 1.25.2 2.45.57 3.57a1 1 0 0 1-.25 1z"/></svg>
    <span>5550147823</span>
  </div>
  <div class="abs email">
    <svg width="24" height="16" viewBox="0 0 24 16" aria-hidden="true"><rect x="1" y="1" width="22" height="14" fill="var(--blue)"/><path d="M1 1l11 8 11-8M1 15l8-7M23 15l-8-7" fill="none" stroke="#fff" stroke-width="1.6"/></svg>
    <span>hello@riverbendtrusted.com</span>
  </div>
  <div class="abs web">www.riverbendtrusted.com</div>
  <div class="abs base-line"></div>

</main>
</body>
</html>
```